Business Card Design

We need a business card design that can also be aplied for postcards. We are a small indie record company that also do consulting, and development of independat artitst . I already have the name and the basic idea of what i am looking for but i am open to any suggestion.
Info for the card
Name of the company : Velmora Records
NAME : Tomas Invaldi
PHONE : 208-5536142
EMAIL : hello@velmorarecords.example
WEB: www.velmorarecords.example
Target Market(s)
Male - Female independent musicians ages 18 to 45
Industry/Entity Type
Record Company
Contact Information for Business Card
Independant records company that also works in consulting for music business models for independent artists
Look and feel
Each slider illustrates characteristics of the customer's brand and the style your logo design should communicate.

```html
<!DOCTYPE html>
<html lang="en">
<head>
<meta charset="utf-8">
<title>Velmora Records – Business Card</title>
<link rel="stylesheet" href="https://fonts.googleapis.com/css2?family=Ubuntu:wght@400;500;700&display=swap">
<style>
  :root {
    --page-bg: #ecebe8;
    --blue-light: #74b8e4;
    --blue-mid: #3f8ac6;
    --blue-deep: #1f6aa8;
    --ink-blue: #1d68a8;
    --ink-grey: #5b6670;
    --card-white: #ffffff;
  }
  * { box-sizing: border-box; margin: 0; padding: 0; }
  html, body {
    width: 1200px; height: 900px; overflow: hidden;
    background: var(--page-bg);
    font-family: "Ubuntu", sans-serif;
  }
  .stage {
    width: 1200px; height: 900px;
    display: flex; align-items: center; justify-content: center; gap: 40px;
  }
  .card {
    width: 540px; height: 309px; position: relative; overflow: hidden;
    border-radius: 3px;
    box-shadow: 0 6px 18px rgba(0,0,0,.18);
  }
  /* Front */
  .card--front {
    background: radial-gradient(ellipse at 55% 50%, var(--blue-light) 0%, var(--blue-mid) 55%, var(--blue-deep) 100%);
    display: flex; align-items: center; justify-content: center;
  }
  .brand {
    display: flex; align-items: center; gap: 14px;
    font-weight: 700; letter-spacing: .5px;
  }
  .brand__dot { border-radius: 50%; flex: none; }
  .brand--front { color: var(--card-white); font-size: 40px; }
  .brand--front .brand__dot { width: 34px; height: 34px; background: var(--card-white); }
  /* Back */
  .card--back { background: var(--card-white); }
  .card__band {
    position: absolute; left: 0; right: 0; bottom: 0; height: 26px;
    background: linear-gradient(90deg, var(--blue-deep) 0%, var(--blue-light) 55%, var(--blue-deep) 100%);
  }
  .brand--back {
    position: absolute; left: 26px; top: 150px;
    flex-direction: column; align-items: flex-start; gap: 8px;
    color: var(--ink-blue); font-size: 30px; line-height: 1.05;
  }
  .brand--back .brand__dot { width: 22px; height: 22px; background: var(--ink-blue); }
  .person {
    position: absolute; left: 250px; top: 54px;
    color: var(--ink-blue); font-size: 30px; font-weight: 400;
  }
  .contact {
    position: absolute; left: 250px; top: 132px;
    list-style: none; color: var(--ink-grey); font-size: 17px;
  }
  .contact li { display: flex; align-items: center; gap: 8px; margin-bottom: 10px; }
  .contact svg { width: 14px; height: 14px; flex: none; fill: var(--ink-grey); }
</style>
</head>
<body>
<main class="stage">
  <section class="card card--front" aria-label="Card front">
    <div class="brand brand--front">
      <span class="brand__dot"></span>
      <span class="brand__name">Velmora Records</span>
    </div>
  </section>

  <section class="card card--back" aria-label="Card back">
    <div class="brand brand--back">
      <span class="brand__dot"></span>
      <span class="brand__name">Velmora<br>Records</span>
    </div>
    <h1 class="person">Tomas Invaldi</h1>
    <ul class="contact">
      <li>
        <svg viewBox="0 0 16 16" aria-hidden="true"><path d="M3.6 1.5l2.3 2.8-1.3 1.6c.9 2 2.5 3.6 4.5 4.5l1.6-1.3 2.8 2.3-1.6 2.1C6.5 13.3 2.7 9.5 1.5 3.1z"/></svg>
        <span>208-5536142</span>
      </li>
      <li>
        <svg viewBox="0 0 16 16" aria-hidden="true"><path d="M1 3h14v10H1zm1.5 1.5v.3L8 8.6l5.5-3.8v-.3zm0 2.1v4.9h11V6.6L8 10.4z"/></svg>
        <span>hello@velmorarecords.example</span>
      </li>
      <li>
        <svg viewBox="0 0 16 16" aria-hidden="true"><path d="M8 1a7 7 0 100 14A7 7 0 008 1zm0 1.5c.8 0 1.7 1.6 2 4H6c.3-2.4 1.2-4 2-4zM5.9 8h4.2c-.1 2.8-1.1 5.5-2.1 5.5S6 10.8 5.9 8zM2.6 7.5a5.5 5.5 0 012.8-4.3c-.5 1.1-.9 2.6-1 4.3zm0 1h1.8c.1 1.7.5 3.2 1 4.3a5.5 5.5 0 01-2.8-4.3zm8.9-1c-.1-1.7-.5-3.2-1-4.3a5.5 5.5 0 012.9 4.3zm0 1h1.9a5.5 5.5 0 01-2.9 4.3c.5-1.1.9-2.6 1-4.3z"/></svg>
        <span>www.velmorarecords.example</span>
      </li>
    </ul>
    <div class="card__band"></div>
  </section>
</main>
</body>
</html>
```